Halworth Builds, Carpentry Services

Business card for carpentry business in the Sunshine Coast.

Business card layout required using logo provided - provided both PDF copy and AI. Please let me know if you would like a the files for the logo symbol and text by itself.

Business Colours are grey, blue and white. The font colours codes for this design are Blue Hex # 00B4E6 and Hex # 39393B for the gray colour.

FYI font for logo is Gotham Bold.

Preference for a clean and striking layout that is simple and elegant.

Target Market(s)

Young Families, retirees, young couples requiring assistance with small to medium works/renovations on the Sunshine Coast.

Industry/Entity Type

Construction

Contact Information for Business Card

Dean Halworth
Carpenter
0481356027
dean@halworthbuilds.com.au
Tidewater Bay, Coral Coast
RHLA Licensed Carpenter (In smaller font)

Font styles to use
Sans Serif

Colors

Designer to choose colors to be used in the design.

Requirements
Must have
• Logo provided must appear on the card, preferably on one side of the card by itself with the text on the alternate side
Nice to have
• Text on the other side of card, maybe grey background and white font here but happy for the designer to provide ideas here.
Should not have
• Use of other colours, other than the ones provided - white, grey and blue. Black optional.

```html
<!DOCTYPE html>
<html lang="en">
<head>
<meta charset="utf-8">
<title>Halworth Builds – Business Card</title>
<link href="https://fonts.googleapis.com/css2?family=Montserrat:wght@400;700&family=Arimo:wght@400&display=swap" rel="stylesheet">
<style>
  :root {
    --blue: #00B4E6;
    --card-grey: #39393B;
    --backdrop: #1e2024;
    --white: #ffffff;
  }
  * { margin: 0; padding: 0; box-sizing: border-box; }
  html, body {
    width: 1200px; height: 1000px; overflow: hidden;
    background: var(--backdrop);
  }
  .canvas {
    width: 1200px; height: 1000px;
    display: flex; flex-direction: column; align-items: center; justify-content: center;
    gap: 36px;
  }
  .card {
    position: relative;
    width: 760px; height: 434px;
    background: var(--card-grey);
    box-shadow: 0 10px 30px rgba(0,0,0,0.45);
  }
  /* Front */
  .card-front { display: flex; align-items: center; justify-content: center; }
  .brand-mark { display: flex; align-items: center; gap: 18px; }
  .brand-square { width: 34px; height: 34px; background: var(--blue); flex: none; }
  .brand-name {
    font-family: "Montserrat", sans-serif; font-weight: 700;
    font-size: 44px; letter-spacing: 2px; color: var(--blue); text-transform: uppercase;
    white-space: nowrap;
  }
  /* Back */
  .brand-name-small {
    position: absolute; top: 96px; right: 56px;
    font-family: "Montserrat", sans-serif; font-weight: 700;
    font-size: 26px; letter-spacing: 1.5px; color: var(--blue); text-transform: uppercase;
    white-space: nowrap;
  }
  .contact-block { position: absolute; left: 60px; top: 168px; color: var(--white); }
  .person-name {
    font-family: "Montserrat", sans-serif; font-weight: 700;
    font-size: 30px; line-height: 1.2; color: var(--blue);
  }
  .person-role {
    font-family: "Montserrat", sans-serif; font-weight: 400;
    font-size: 19px; margin-top: 4px;
  }
  .role-rule { width: 40px; height: 2px; background: var(--blue); margin: 8px 0 10px; }
  .licence { font-family: "Arimo", sans-serif; font-size: 12px; margin-bottom: 10px; }
  .contact-list { list-style: none; font-family: "Arimo", sans-serif; font-size: 18px; }
  .contact-list li { display: flex; align-items: center; gap: 12px; height: 28px; white-space: nowrap; }
  .contact-list svg { width: 16px; height: 16px; fill: var(--blue); flex: none; }
</style>
</head>
<body>
<main class="canvas">
  <section class="card card-front">
    <div class="brand-mark">
      <span class="brand-square"></span>
      <span class="brand-name">Halworth Builds</span>
    </div>
  </section>

  <section class="card card-back">
    <div class="brand-name-small">Halworth Builds</div>
    <div class="contact-block">
      <h1 class="person-name">Dean Halworth</h1>
      <p class="person-role">Carpenter</p>
      <div class="role-rule"></div>
      <p class="licence">RHLA Licensed Carpenter</p>
      <ul class="contact-list">
        <li><svg viewBox="0 0 16 16"><path d="M3.5 1l2.5 3-1.5 1.8c.8 1.9 2.3 3.4 4.2 4.2L10.5 8.5l3 2.5-1.2 2.8C7 13.5 2.5 9 2.2 3.7z"/></svg>0481356027</li>
        <li><svg viewBox="0 0 16 16"><path d="M1 3h14v10H1zM2.5 4.5v.4L8 9l5.5-4.1v-.4zM2.5 6.7v4.8h11V6.7L8 10.8z"/></svg>dean@halworthbuilds.com.au</li>
        <li><svg viewBox="0 0 16 16"><path d="M8 1a7 7 0 1 0 0 14A7 7 0 0 0 8 1zm-1 2.2c-.6 1-1.4 1.4-2.2 1.9.4 1 1.6 1.3 2 2.3-.3 1 .4 2 1 2.6-.3 1.1-.9 2-1.2 2.8A5.5 5.5 0 0 1 7 3.2zm3.2.8a5.5 5.5 0 0 1 2.4 6.3c-.9-.4-1.1-1.5-2-1.8-.6-.9-.1-2 .4-2.6-.7-.4-1.1-1-.8-1.9z"/></svg>www.halworthbuilds.com.au</li>
        <li><svg viewBox="0 0 16 16"><path d="M8 1a5 5 0 0 0-5 5c0 3.6 5 9 5 9s5-5.4 5-9a5 5 0 0 0-5-5zm0 7a2 2 0 1 1 0-4 2 2 0 0 1 0 4z"/></svg>Tidewater Bay, Coral Coast</li>
      </ul>
    </div>
  </section>
</main>
</body>
</html>
```